K&T Fixit and Rebuild general contracting business card design

I already have a logo that I want to use and I need a card that uses that logo and color scheme on the front with the address phone numbers and email and on the back a place for technicians to write in their name and phone number when they hand it out. It will need the License number of License #KTFXTRB318QN.
It should say General Contractor under the company name. The address is
4417 NE 3rd Ave, Ste D246
Vancouver, WA 98612
www.kandtfixitandrebuild.example
office@kandtfixitandrebuild.example
360-555-0182 is the telephone number
360-555-0149 is the fax number

Target Market(s)

Homeowners needing remodel work or repairs in their home.

Industry/Entity Type

Construction

Contact Information for Business Card

Business name, address, phone number, license number, fax number, email, and website on the front and a place to fill in technician's name and number

Font styles to use
Serif

Requirements
Must have
• Business name, address, phone number, license number, fax number, email, and website on the front and a place to fill in technician's name and number
Nice to have
• I uploaded an example of a front that is good.
Should not have
• Froo froo or extra embellishments.

```html
<!DOCTYPE html>
<html lang="en">
<head>
<meta charset="utf-8">
<title>K&amp;T Fixit and Rebuild – Business Card</title>
<link rel="stylesheet" href="https://fonts.googleapis.com/css2?family=Roboto+Slab:wght@400;500;700&display=swap">
<style>
  :root {
    --page: #2b2b2b;
    --wood-light: #cf8137;
    --wood-mid: #bd6c25;
    --wood-dark: #a85a1b;
    --logo-brown: #8a3d10;
    --charcoal: #2f2f2f;
    --paper: #f1f1f1;
    --ink: #151515;
    --rule: #6a6a6a;
    --white: #ffffff;
  }
  * { margin: 0; padding: 0; box-sizing: border-box; }
  html, body { width: 1200px; height: 1138px; overflow: hidden; }
  body {
    background: var(--page);
    font-family: "Roboto Slab", serif;
    position: relative;
  }
  .card {
    position: absolute;
    border-radius: 14px;
    overflow: hidden;
  }

  /* Front card */
  .card-front {
    left: 274px; top: 186px; width: 623px; height: 376px;
  }
  .wood {
    position: absolute; inset: 0;
    background: linear-gradient(170deg, var(--wood-light) 0%, var(--wood-mid) 55%, var(--wood-dark) 100%);
  }
  .front-brand {
    position: absolute; left: 0; right: 0; top: 0; height: 284px;
    display: flex; flex-direction: column; align-items: center; justify-content: center;
    gap: 10px;
  }
  .front-brand .brand-name {
    font-weight: 700; font-size: 38px; color: var(--logo-brown);
  }
  .front-brand .brand-role {
    font-weight: 700; font-size: 22px; color: var(--logo-brown);
    letter-spacing: 2px; text-transform: uppercase;
  }
  .tagline-band {
    position: absolute; left: 0; right: 0; top: 284px; height: 37px;
    background: var(--charcoal);
    color: #e8e8e8; font-size: 15.5px;
    display: flex; align-items: center; justify-content: center;
  }
  .front-footer {
    position: absolute; left: 0; right: 0; top: 321px; bottom: 0;
    display: flex; align-items: center; justify-content: center; gap: 20px;
    font-size: 15px; color: var(--ink);
  }

  /* Back card */
  .card-back {
    left: 276px; top: 608px; width: 618px; height: 374px;
    background: var(--paper);
  }
  .back-art { position: absolute; inset: 0; }
  .back-brand {
    position: absolute; left: 160px; top: 187px;
    transform: translate(-50%, -50%) rotate(-90deg);
    white-space: nowrap;
    font-weight: 500; font-size: 23px; color: var(--white);
  }
  .contact {
    position: absolute; left: 276px; top: 44px; width: 326px; color: var(--ink);
  }
  .write-in {
    display: flex; align-items: flex-end; height: 32px;
    font-weight: 700; font-size: 15px;
  }
  .write-in .label { flex: none; width: 92px; }
  .write-in .blank { flex: 1; border-bottom: 1px solid var(--rule); height: 1px; margin-bottom: 4px; }
  .address { font-size: 15px; line-height: 22px; margin-top: 20px; }
  .lines { margin-top: 10px; font-size: 15px; }
  .line { display: flex; align-items: center; height: 23px; white-space: nowrap; }
  .line svg { width: 15px; height: 15px; margin-right: 10px; flex: none; }
  .line .fax { margin-left: 16px; }
  .back-license {
    position: absolute; left: 276px; top: 316px; height: 42px;
    display: flex; align-items: center;
    font-size: 15px; color: var(--ink);
  }
</style>
</head>
<body>

<section class="card card-front" aria-label="Card front">
  <div class="wood" role="img" aria-label="Warm wood grain texture"></div>
  <div class="front-brand">
    <span class="brand-name">K&amp;T Fixit and Rebuild</span>
    <span class="brand-role">General Contractor</span>
  </div>
  <div class="tagline-band">Home Maintenance &amp; Remodeling Contractors</div>
  <div class="front-footer">
    <span>License #KTFXTRB318QN</span><span>|</span><span>www.kandtfixitandrebuild.example</span>
  </div>
</section>

<section class="card card-back" aria-label="Card back">
  <svg class="back-art" width="618" height="374" viewBox="0 0 618 374">
    <defs>
      <linearGradient id="woodGrad" x1="0" y1="0" x2="1" y2="1">
        <stop offset="0" stop-color="#cf8137"/>
        <stop offset="1" stop-color="#b0601e"/>
      </linearGradient>
    </defs>
    <rect x="0" y="316" width="618" height="42" fill="url(#woodGrad)"/>
    <path d="M0 0 H196 Q300 187 194 374 H0 Z" fill="url(#woodGrad)" role="img" aria-label="Wood grain edge"/>
    <path d="M0 0 H186 Q288 187 184 374 H0 Z" fill="#2f2f2f" role="img" aria-label="Dark wood grain texture"/>
  </svg>
  <div class="back-brand">K&amp;T Fixit and Rebuild</div>

  <div class="contact">
    <div class="write-in"><span class="label">Technician</span><span class="blank"></span></div>
    <div class="write-in"><span class="label">Phone</span><span class="blank"></span></div>
    <div class="address">4417 NE 3rd Ave, Ste D246<br>Vancouver, WA 98612</div>
    <div class="lines">
      <div class="line">
        <svg viewBox="0 0 16 16" aria-hidden="true"><path d="M1 6 Q8 0 15 6 L13 8 L11 6 V5 H5 V6 L3 8 Z M4 9 H12 L13 14 H3 Z" fill="#151515"/></svg>
        <span>360-555-0182</span>
        <svg class="fax" viewBox="0 0 16 16" aria-hidden="true"><rect x="4" y="1" width="8" height="4" fill="#151515"/><rect x="1" y="6" width="14" height="6" rx="1" fill="#151515"/><rect x="4" y="10" width="8" height="5" fill="#151515"/><rect x="5" y="11" width="6" height="3" fill="#f1f1f1"/></svg>
        <span>360-555-0149</span>
      </div>
      <div class="line">
        <svg viewBox="0 0 16 16" aria-hidden="true"><rect x="1" y="3" width="14" height="10" fill="#151515"/><path d="M1.5 3.5 L8 9 L14.5 3.5 M1.5 12.5 L6 8 M14.5 12.5 L10 8" stroke="#f1f1f1" stroke-width="1.2" fill="none"/></svg>
        <span>www.kandtfixitandrebuild.example</span>
      </div>
      <div class="line">
        <svg viewBox="0 0 16 16" aria-hidden="true"><circle cx="8" cy="8" r="7" fill="none" stroke="#151515" stroke-width="1.4"/><ellipse cx="8" cy="8" rx="3" ry="7" fill="none" stroke="#151515" stroke-width="1.2"/><path d="M1 8 H15 M2.5 4.5 H13.5 M2.5 11.5 H13.5" stroke="#151515" stroke-width="1.2"/></svg>
        <span>office@kandtfixitandrebuild.example</span>
      </div>
    </div>
  </div>
  <div class="back-license">License #KTFXTRB318QN</div>
</section>

</body>
</html>
```